Cobre Ridge Grill Rub bottle label design

I need a design for 2 different seasoning bottles
looking for something classy and clean.
One of the spices will be named TOPGRD. I would like to see a creative design for the name. I included the label dimensions as an attachment. I also included a picture of some spice bottles I saw only that I like. they dont have to be exactly like that but i like the matte black with the "foil" metallic colors on the bottom. I also want to include somewhere on the front of the bottle that I am a 3x world BBQ champion. I also included my logo on the attachments on the bottom. if you look at the label dimensions attachment there is an area for the nutrition fact and upc barcode. I have that info that i can give you and just plug it into the design. Also on the other side panel I have a brief description that will go on that side that I can provide you as well so you can plug it in.
Target Market(s)
Retail stores
Requirements
Must have
- My logo. I can provide to you.
Should say 3x BBQ world champion somewhere on front of the bottle
Name of the Seasoning TOPGRD and Dorado. 2 different
A brief description/story that will go on the side panel. I will send that to you.
Should have Texas incorporated into the design not so prominent.
Nice to have
- Figures or shapes of animals like a chicken, pig, cow. Small so that people can see what they can use that seasoning for.

```html
<!DOCTYPE html>
<html lang="en">
<head>
<meta charset="utf-8">
<title>Cobre Ridge Grill Rub – Seasoning Labels</title>
<link href="https://fonts.googleapis.com/css2?family=Allura&family=Cinzel:wght@600&family=Open+Sans:wght@500&family=Ultra&display=swap" rel="stylesheet">
<style>
  :root {
    --canvas: #ffffff;
    --band: #ffffff;
    --navy: #14284a;
    --navy-light: #1a3358;
    --red: #8c1418;
    --red-light: #a5191d;
    --name-red: #c92a2c;
    --name-blue: #5090b3;
    --gold: #c9a14a;
    --gold-light: #e6c877;
    --logo-ink: #1d2f5c;
    --icon-blue: #5a9bbf;
    --icon-red: #d23a36;
  }
  html, body {
    margin: 0;
    width: 1200px;
    height: 816px;
    overflow: hidden;
    background: var(--canvas);
  }
  .canvas {
    position: relative;
    width: 1200px;
    height: 816px;
    display: flex;
    justify-content: center;
    align-items: center;
    gap: 140px;
  }
  .label {
    width: 420px;
    height: 480px;
    display: flex;
    flex-direction: column;
    box-shadow: 0 6px 24px rgba(0,0,0,0.12);
  }
  .brand-band {
    height: 104px;
    background: var(--band);
    display: flex;
    align-items: center;
    justify-content: center;
    gap: 12px;
  }
  .brand-mark {
    width: 14px;
    height: 14px;
    background: var(--logo-ink);
  }
  .brand-name {
    font-family: "Cinzel", serif;
    font-weight: 600;
    font-size: 25px;
    color: var(--logo-ink);
    letter-spacing: 0.5px;
  }
  .panel {
    flex: 1;
    display: flex;
    flex-direction: column;
    align-items: center;
    padding-top: 0;
  }
  .label--topgrd .panel { background: linear-gradient(90deg, var(--navy) 0%, var(--navy-light) 50%, var(--navy) 100%); }
  .label--dorado .panel { background: linear-gradient(90deg, var(--red) 0%, var(--red-light) 50%, var(--red) 100%); }
  .seal {
    width: 104px;
    height: 104px;
    margin-top: -12px;
  }
  .tagline {
    display: flex;
    align-items: center;
    gap: 10px;
    margin-top: 0;
    font-family: "Allura", cursive;
    font-size: 36px;
    line-height: 1;
  }
  .tagline::before, .tagline::after {
    content: "";
    width: 52px;
    height: 1px;
    background: currentColor;
    opacity: 0.7;
  }
  .label--topgrd .tagline { color: var(--name-red); }
  .label--dorado .tagline { color: #5a1010; }
  .product-name {
    font-family: "Ultra", serif;
    font-size: 64px;
    line-height: 1;
    margin-top: 4px;
    letter-spacing: 1px;
  }
  .label--topgrd .product-name { color: var(--name-red); }
  .label--dorado .product-name { color: var(--name-blue); }
  .subtitle {
    font-family: "Allura", cursive;
    font-size: 44px;
    color: var(--gold);
    margin-top: 10px;
    line-height: 1;
  }
  .use-with {
    position: relative;
    margin-top: 22px;
    width: 156px;
    height: 40px;
    border: 1px solid;
    border-top: none;
    display: flex;
    align-items: center;
    justify-content: center;
  }
  .use-with-title {
    position: absolute;
    top: -8px;
    left: 0;
    right: 0;
    display: flex;
    align-items: center;
    gap: 6px;
    font-family: "Open Sans", sans-serif;
    font-weight: 500;
    font-size: 12px;
    line-height: 1;
  }
  .use-with-title::before, .use-with-title::after {
    content: "";
    flex: 1;
    height: 1px;
    background: currentColor;
  }
  .label--topgrd .use-with { color: var(--icon-blue); border-color: var(--icon-blue); }
  .label--dorado .use-with { color: var(--icon-red); border-color: var(--icon-red); }
  .animal-icons {
    width: 120px;
    height: 24px;
    margin-top: 6px;
    border-radius: 3px;
    opacity: 0.55;
    background: currentColor;
  }
</style>
</head>
<body>
<main class="canvas">

  <section class="label label--topgrd">
    <header class="brand-band">
      <span class="brand-mark"></span>
      <span class="brand-name">Cobre Ridge Grill Rub</span>
    </header>
    <div class="panel">
      <svg class="seal" viewBox="0 0 100 100" aria-hidden="true">
        <defs>
          <radialGradient id="goldA" cx="40%" cy="35%" r="70%">
            <stop offset="0" stop-color="var(--gold-light)"/>
            <stop offset="1" stop-color="#9b7428"/>
          </radialGradient>
        </defs>
        <circle cx="50" cy="50" r="44" fill="url(#goldA)"/>
      </svg>
      <div class="tagline">Texas inspired</div>
      <h1 class="product-name">TOPGRD</h1>
      <div class="subtitle">Hearbs &amp; Spices</div>
      <div class="use-with">
        <span class="use-with-title">USE WITH</span>
        <div class="animal-icons" role="img" aria-label="Small cow, pig and chicken silhouettes"></div>
      </div>
    </div>
  </section>

  <section class="label label--dorado">
    <header class="brand-band">
      <span class="brand-mark"></span>
      <span class="brand-name">Cobre Ridge Grill Rub</span>
    </header>
    <div class="panel">
      <svg class="seal" viewBox="0 0 100 100" aria-hidden="true">
        <defs>
          <radialGradient id="goldB" cx="40%" cy="35%" r="70%">
            <stop offset="0" stop-color="var(--gold-light)"/>
            <stop offset="1" stop-color="#9b7428"/>
          </radialGradient>
        </defs>
        <circle cx="50" cy="50" r="44" fill="url(#goldB)"/>
      </svg>
      <div class="tagline">Texas inspired</div>
      <h1 class="product-name">DORADO</h1>
      <div class="subtitle">Hearbs &amp; Spices</div>
      <div class="use-with">
        <span class="use-with-title">USE WITH</span>
        <div class="animal-icons" role="img" aria-label="Small cow, pig and chicken silhouettes"></div>
      </div>
    </div>
  </section>

</main>
</body>
</html>
```